Creative Magazine Ad - fusing comfort, culture and cuisine for a food supply company

Hello and welcome to this project!

We need an ad for our company, Kela Supply Co, that is going to be in a magazine read by the Australian Army based in Papua New Guinea.

We want an ad that makes people stop and look. The key message is that even though Papua New Guinea is exotic, the food can be the same (as in Australia). And we want to show off what our company does – supplying great food that caters for all.

Your design should include:

Size:
• 1 page at 15cm height x 19.6cm width
Pictures:
• Our logo – Kela Supply Co – where people can see it
• Pictures or elements that capture the tropical landscape, tribal culture and or essence of Papua New Guinea mixed with pictures of Australian food like barbeque, steaks, pies, roast vegetables etc.
Text to add:
• Title: "Taste of Home in the Tropics: Your Australian Culinary Guide in Papua New Guinea”
• Message: "Our mission is to manufacture and procure a diverse range of high-quality food products, catering to the unique needs of defence camps, and supplying small to large wholesalers, retailers, restaurants, hotels, and caterers throughout Papua New Guinea. We are dedicated to supporting our defence forces with the comforts of home, while serving the broader community with exceptional culinary offerings."
• And our contact details:
+675 314 2691
www.ksv.com.pg
sales@kelasupplyco.com.pg

What we need:
• A graphic for printing for the magazine.
• A digital version to use online.

Thanks again – any questions please ask :)

A Bit About Us
Kela Supply Co Ltd is a 100% PNG-owned and managed business and is proud to be one of the largest food supply companies in the country. Our ability to supply a wide range of premium imported, local and in-house manufactured products from our Butchery and Bakery has contributed to the rock-solid reputation for quality and services that Kela Supply now enjoys throughout PNG.

We are proud to also sell our wide range of products through our retail outlets (Tova Grill Haus, Tova Crust Haus and Lute Grill Haus) and our popular Quick Service Restaurants (Reef Stacker and Orb Tart Nook). Our Catering division (Tova Welo Catering) owns a vast array of commercial catering equipment and has experience catering for large-scale events in PNG. We are the only company in Papua New Guinea that has the technology to provide “tamper proof” cold and hot individual meal solutions that can be delivered in temperature-controlled vehicles to locations in Port Moresby but also as a solution to large-scale mining camp catering needs.

```html
<!DOCTYPE html>
<html lang="en">
<head>
<meta charset="utf-8">
<title>Kela Supply Co – Taste of Home in the Tropics</title>
<link rel="stylesheet" href="https://fonts.googleapis.com/css2?family=Raleway:wght@800;900&family=Bebas+Neue&family=Alegreya+Sans:wght@400&family=Roboto+Condensed:ital,wght@1,700&display=swap">
<style>
  :root {
    --brand-red: #ee1c1c;
    --ink: #111111;
    --body-grey: #555555;
    --contact-grey: #4a4a4a;
    --paper: #ffffff;
  }
  * { margin: 0; padding: 0; box-sizing: border-box; }
  html, body { width: 1200px; height: 918px; overflow: hidden; background: var(--paper); }
  .ad { position: relative; width: 1200px; height: 918px; background: var(--paper); overflow: hidden; }

  .brand { position: absolute; left: 170px; top: 68px; width: 230px; display: flex; align-items: center; justify-content: center; gap: 10px; }
  .brand-dot { width: 22px; height: 22px; border-radius: 50%; background: var(--brand-red); flex: none; }
  .brand-name { font-family: "Raleway", sans-serif; font-weight: 800; font-size: 30px; color: var(--ink); white-space: nowrap; }
  .cert-badge { position: absolute; left: 322px; top: 44px; width: 56px; height: 22px; background: var(--brand-red); border-radius: 3px; }
  .tagline { position: absolute; left: 0; width: 568px; top: 156px; text-align: center; font-family: "Roboto Condensed", sans-serif; font-style: italic; font-weight: 700; font-size: 12.5px; color: var(--ink); }

  .headline { position: absolute; left: 0; top: 0; font-family: "Raleway", sans-serif; font-weight: 900; color: var(--brand-red); letter-spacing: -0.5px; }
  .headline-line1 { position: absolute; left: 56px; top: 196px; font-size: 60px; line-height: 1; white-space: nowrap; }
  .headline-bar { position: absolute; left: 38px; top: 287px; width: 472px; height: 56px; background: var(--ink); }
  .headline-line2 { position: absolute; left: 70px; top: 258px; font-size: 60px; line-height: 1; white-space: nowrap; }

  .subhead { position: absolute; left: 38px; width: 472px; top: 350px; text-align: center; font-family: "Bebas Neue", sans-serif; font-size: 38px; line-height: 42px; letter-spacing: 2.4px; color: var(--brand-red); }

  .mission { position: absolute; left: 62px; top: 486px; width: 444px; font-family: "Alegreya Sans", sans-serif; font-size: 18px; line-height: 21px; letter-spacing: 1.1px; color: var(--body-grey); text-align: justify; }

  .contact { position: absolute; right: 678px; top: 800px; text-align: right; font-family: "Alegreya Sans", sans-serif; font-size: 22px; line-height: 24px; letter-spacing: 2px; color: var(--contact-grey); }
  .contact span { display: block; }
  .footer-bar { position: absolute; left: 97px; top: 884px; width: 425px; height: 34px; background: var(--brand-red); }

  .photo-panel { position: absolute; left: 565px; top: 0; width: 604px; height: 918px; background: var(--brand-red); }
  .hero-photo { position: absolute; left: 35px; top: 105px; width: 511px; height: 708px;
    background: radial-gradient(ellipse at 55% 60%, #6b2f14 0%, #4a1e0c 35%, transparent 60%),
                linear-gradient(180deg, #c9611a 0%, #e88a2a 25%, #7a3a16 55%, #2b140a 100%); }
  .photo-frame { position: absolute; left: 72px; top: 74px; width: 457px; height: 770px; border: 2px solid var(--paper); }
</style>
</head>
<body>
<main class="ad">
  <div class="brand">
    <span class="brand-dot"></span>
    <span class="brand-name">Kela Supply</span>
  </div>
  <div class="cert-badge" aria-hidden="true"></div>
  <p class="tagline">“100% PNG Owned &amp; Operated”</p>

  <h1 class="headline">
    <span class="headline-line1">Taste of Home</span>
    <span class="headline-bar" aria-hidden="true"></span>
    <span class="headline-line2">in the Tropics</span>
  </h1>

  <h2 class="subhead">Your Australian Culinary<br>Guide in Papua New Guinea</h2>

  <p class="mission">Our mission is to manufacture and procure a diverse range of high-quality food products, catering to the unique needs of defence camps, and supplying small to large wholesalers, retailers, restaurants, hotels, and caterers throughout Papua New Guinea. We are dedicated to supporting our defence forces with the comforts of home, while serving the broader community with exceptional culinary offerings.</p>

  <address class="contact">
    <span>+675 314 2691</span>
    <span>www.ksv.com.pg</span>
    <span>sales@kelasupplyco.com.pg</span>
  </address>
  <div class="footer-bar" aria-hidden="true"></div>

  <section class="photo-panel">
    <div class="hero-photo" role="img" aria-label="Close-up of a grilled steak topped with rosemary on a barbecue grill over flames"></div>
    <div class="photo-frame" aria-hidden="true"></div>
  </section>
</main>
</body>
</html>
```